" Somos um provedor de internet que fornece principalmente o serviço de internet por fibra óptica. Também temos TV por assinatura via satélite e telefonia IP "

```html
<!DOCTYPE html>
<html lang="pt-BR">
<head>
<meta charset="utf-8">
<title>Luma Fibra — Internet fibra óptica</title>
<link href="https://fonts.googleapis.com/css2?family=Open+Sans:ital,wght@0,400;0,600;0,700;1,400;1,600&display=swap" rel="stylesheet">
<style>
  :root{
    --blue:#2f8fd8;
    --blue-dark:#0b2a66;
    --navy:#06183f;
    --ink:#333a44;
    --muted:#8a9099;
    --line:#e6e8eb;
    --band:#f1f2f4;
    --white:#ffffff;
  }
  *{margin:0;padding:0;box-sizing:border-box}
  html,body{width:1200px;height:1200px;overflow:hidden;background:var(--white)}
  body{font-family:"Open Sans",Arial,sans-serif;color:var(--ink);position:relative}
  .wrap{position:absolute;left:154px;width:892px}

  .topbar{top:0;height:20px;display:flex;justify-content:space-between;align-items:center;font-size:8px;color:var(--muted);border-bottom:1px solid var(--line)}
  .topbar .social{display:flex;gap:14px}
  .topbar .social span{width:7px;height:7px;border-radius:50%;background:#b9bec5;display:block}

  .header{top:20px;height:56px;display:flex;justify-content:space-between;align-items:center}
  .brand{display:flex;align-items:center;gap:8px;font-weight:700;font-size:16px;color:var(--navy);letter-spacing:.5px}
  .brand i{width:22px;height:22px;background:var(--blue-dark);display:block}
  .nav{display:flex;gap:26px;font-size:9px;color:var(--muted);text-transform:uppercase}

  .hero{top:77px;height:302px;background:radial-gradient(circle at 82% 35%,#3d8fe6 0%,#1449a8 28%,#0a2660 60%,#061638 100%)}
  .hero h1{position:absolute;left:236px;top:130px;color:var(--white);font-size:30px;font-weight:700}
  .hero h2{position:absolute;left:236px;top:167px;color:var(--white);font-size:20px;font-weight:400;font-style:italic}
  .hero p{position:absolute;left:236px;top:200px;width:300px;color:#cfe0f7;font-size:9px;line-height:1.5}
  .hero .btns{position:absolute;left:236px;top:230px;display:flex;gap:12px}
  .btn{font-size:8px;font-weight:700;text-transform:uppercase;padding:6px 14px;color:var(--white)}
  .btn.solid{background:var(--blue)}
  .btn.ghost{background:var(--white);color:var(--blue-dark)}
  .hero small{position:absolute;left:236px;bottom:12px;color:#c2d3ee;font-size:7px}

  .segments{top:425px;display:flex;justify-content:center;gap:42px}
  .seg{width:120px;text-align:center}
  .seg .ico{width:56px;height:56px;border-radius:50%;background:#eef4fb;margin:0 auto 10px;display:flex;align-items:center;justify-content:center}
  .seg .ico.active{background:var(--blue);box-shadow:0 0 0 4px #d6e7f7}
  .seg h3{font-size:9px;font-weight:600;color:var(--ink);margin-bottom:5px}
  .seg p{font-size:7px;color:var(--muted);line-height:1.5}

  .offers{top:607px;height:113px;background:var(--band);text-align:center;padding-top:30px}
  .offers h2{font-size:18px;font-style:italic;font-weight:600;color:var(--blue-dark)}
  .offers p{font-size:8px;color:var(--muted);width:300px;margin:8px auto 0;line-height:1.5}

  .gallery{top:725px;height:298px;display:grid;grid-template-columns:repeat(4,1fr);grid-template-rows:1fr 1fr;gap:4px}
  .tile{position:relative}
  .t1{background:linear-gradient(180deg,#8fa8c4,#5d6a78)}
  .t2{background:linear-gradient(180deg,#2c6fb5,#0e2f64)}
  .t3{background:linear-gradient(180deg,#9cc0e2,#6d7a6a)}
  .t4{background:linear-gradient(180deg,#86b2dc,#a89b84)}
  .t5{background:linear-gradient(180deg,#7e8ea5,#5b5148)}
  .t6{background:linear-gradient(180deg,#a7b6c8,#6c645a)}
  .t7{background:linear-gradient(180deg,#4b79b3,#a2b1c1)}
  .t8{background:linear-gradient(180deg,#2f6fb8,#5f7aa0)}
  .tile .overlay{position:absolute;inset:0;display:flex;flex-direction:column;justify-content:center;align-items:center;background:rgba(12,50,120,.55);color:var(--white)}
  .overlay strong{font-size:12px;font-style:italic;font-weight:400}
  .overlay span{font-size:7px;margin-top:4px;color:#d1def2}

  .happy{top:1027px;height:72px;background:var(--blue);display:flex;align-items:center;justify-content:center;color:var(--white);font-size:15px;font-style:italic}
  .happy b{font-weight:700;margin-left:5px}

  .features{top:1150px;display:flex;justify-content:space-around}
  .feat{display:flex;gap:10px;width:220px}
  .feat h4{font-size:9px;font-weight:600;color:var(--ink)}
  .feat p{font-size:7px;color:var(--muted);line-height:1.5;margin-top:3px}
</style>
</head>
<body>

<div class="wrap topbar">
  <span>Atendimento de segunda a sábado, das 8h às 20h · Central: (11) 4000-1234</span>
  <div class="social"><span></span><span></span><span></span><span></span><span></span></div>
</div>

<header class="wrap header">
  <div class="brand"><i></i>LUMA FIBRA</div>
  <nav class="nav"><span>Início</span><span>A Empresa</span><span>Serviços</span><span>Planos</span><span>Contato</span><span>Suporte</span></nav>
</header>

<section class="wrap hero" role="img" aria-label="Globo terrestre com rede de conexões luminosas sobre um teclado, em tons de azul">
  <h1>Internet fibra óptica</h1>
  <h2>A solução que você precisa!</h2>
  <p>Conexão estável e veloz para sua casa e sua empresa, com suporte técnico local e planos sob medida.</p>
  <div class="btns"><span class="btn solid">Saiba mais</span><span class="btn ghost">Contratar</span></div>
  <small>Instalação em até 48 horas em toda a região atendida</small>
</section>

<section class="wrap segments">
  <div class="seg">
    <div class="ico"><svg width="26" height="26" viewBox="0 0 24 24" fill="#2f8fd8"><path d="M12 3 2 12h3v8h5v-5h4v5h5v-8h3z"/></svg></div>
    <h3>Residências</h3>
    <p>Planos de fibra com alta velocidade para toda a família navegar.</p>
  </div>
  <div class="seg">
    <div class="ico"><svg width="26" height="26" viewBox="0 0 24 24" fill="#2f8fd8"><rect x="3" y="9" width="5" height="12"/><rect x="9.5" y="4" width="5" height="17"/><rect x="16" y="11" width="5" height="10"/></svg></div>
    <h3>Condomínios</h3>
    <p>Rede dedicada para todos os apartamentos com gestão simples e prática.</p>
  </div>
  <div class="seg">
    <div class="ico active"><svg width="26" height="26" viewBox="0 0 24 24" fill="#ffffff"><rect x="4" y="6" width="5" height="15"/><rect x="10" y="3" width="5" height="18"/><rect x="16" y="9" width="4" height="12"/></svg></div>
    <h3>Empresas</h3>
    <p>Link dedicado, telefonia IP e atendimento prioritário para o seu negócio.</p>
  </div>
  <div class="seg">
    <div class="ico"><svg width="26" height="26" viewBox="0 0 24 24" fill="#2f8fd8"><path d="M12 2 2 7v2h20V7z"/><rect x="4" y="10" width="2.5" height="8"/><rect x="8.5" y="10" width="2.5" height="8"/><rect x="13" y="10" width="2.5" height="8"/><rect x="17.5" y="10" width="2.5" height="8"/><rect x="2" y="19" width="20" height="2"/></svg></div>
    <h3>Governo</h3>
    <p>Soluções seguras de conectividade para órgãos e instituições públicas.</p>
  </div>
</section>

<section class="wrap offers">
  <h2>As melhores propostas para você!</h2>
  <p>Conheça nossos planos de internet, TV por assinatura e telefonia IP para cada necessidade.</p>
</section>

<section class="wrap gallery">
  <div class="tile t1" role="img" aria-label="Residência moderna com piscina"></div>
  <div class="tile t2" role="img" aria-label="Edifício residencial de cliente">
    <div class="overlay"><strong>Nome do cliente/empresa</strong><span>Residencial · Condomínio</span></div>
  </div>
  <div class="tile t3" role="img" aria-label="Prédio comercial com jardim"></div>
  <div class="tile t4" role="img" aria-label="Condomínio de torres residenciais"></div>
  <div class="tile t5" role="img" aria-label="Edifício público histórico com colunas"></div>
  <div class="tile t6" role="img" aria-label="Prédio de escritórios"></div>
  <div class="tile t7" role="img" aria-label="Edifício corporativo de vidro branco"></div>
  <div class="tile t8" role="img" aria-label="Torre empresarial envidraçada"></div>
</section>

<section class="wrap happy">Clientes satisfeitos em todo <b>Brasil!</b></section>

<section class="wrap features">
  <div class="feat">
    <svg width="18" height="18" viewBox="0 0 24 24" fill="none" stroke="#8a9099" stroke-width="2"><rect x="6" y="2" width="12" height="20" rx="2"/><line x1="11" y1="18" x2="13" y2="18"/></svg>
    <div><h4>100% Responsive Ready</h4><p>Acesse sua área do cliente em qualquer tela ou dispositivo.</p></div>
  </div>
  <div class="feat">
    <svg width="18" height="18" viewBox="0 0 24 24" fill="none" stroke="#8a9099" stroke-width="2"><circle cx="10" cy="10" r="6"/><line x1="15" y1="15" x2="21" y2="21"/></svg>
    <div><h4>SEO Optimized</h4><p>Encontre nossos planos com facilidade em qualquer buscador.</p></div>
  </div>
  <div class="feat">
    <svg width="18" height="18" viewBox="0 0 24 24" fill="none" stroke="#8a9099" stroke-width="2"><path d="M12 21s-8-5-8-11a4.5 4.5 0 0 1 8-2.8A4.5 4.5 0 0 1 20 10c0 6-8 11-8 11z"/></svg>
    <div><h4>Lovely Design</h4><p>Navegação clara e agradável pensada para você e sua família.</p></div>
  </div>
</section>

</body>
</html>
```